Business card design for a engineering company

I need a double sided business card design for my company "Verdmont Flow Solutions". The card will be used in Malaysia. Sleek and professional, with a little design flare to it.
Information to showcase:
1. Company logo
2. Name, title, phone, email address, website address
3. our products "Pumping technology, Valve & actuation, Air Moving Technology
Example:
Ravi Tanaka
Business manager
ravi.tanaka@verdmont-example.com
www.verdmont-example.com.my
- Pumping technology
- Valve & actuation
- Air moving technology
Target Market(s)
engineers, purchasing managers
Industry/Entity Type
Business
Contact Information for Business Card
Ravi Tanaka
Business manager
ravi.tanaka@verdmont-example.com
www.verdmont-example.com.my
- Pumping technology
- Valve & actuation
- Air moving technology
catch phrase : "Solving flow challenges, exceeding expectations"

```html
<!DOCTYPE html>
<html lang="en">
<head>
<meta charset="utf-8">
<title>Verdmont Flow Solutions – Business Card</title>
<link rel="stylesheet" href="https://fonts.googleapis.com/css2?family=Open+Sans:wght@300;400;600;700&display=swap">
<style>
  :root {
    --teal: #143746;
    --teal-deep: #0e2c39;
    --orange: #f08a24;
    --orange-soft: #f4a55a;
    --yellow: #f7b51c;
    --white: #ffffff;
    --grey-text: #33434c;
    --stage: #e3e4e6;
  }
  * { box-sizing: border-box; margin: 0; padding: 0; }
  html, body {
    width: 1200px; height: 800px; overflow: hidden;
    background: var(--stage);
    font-family: "Open Sans", Arial, sans-serif;
  }
  .card {
    position: absolute;
    top: 252px;
    width: 520px; height: 297px;
    background: var(--white);
    overflow: hidden;
    box-shadow: 0 6px 18px rgba(0,0,0,0.12);
  }
  .card--front { left: 60px; }
  .card--back  { left: 620px; }
  .card__wave { position: absolute; inset: 0; width: 100%; height: 100%; }

  .brand { position: absolute; display: flex; align-items: center; gap: 12px; }
  .brand__dot { width: 36px; height: 36px; border-radius: 50%; flex: none; }
  .brand__name { font-size: 26px; font-weight: 700; line-height: 1; white-space: nowrap; }

  .card--front .brand { left: 36px; top: 30px; color: var(--teal); }
  .card--front .brand__dot { background: var(--teal); }
  .card--back .brand { left: 110px; top: 38px; color: var(--white); }
  .card--back .brand__dot { background: var(--white); }

  .person { position: absolute; left: 36px; top: 88px; }
  .person__name { font-size: 22px; color: var(--orange); line-height: 1.1; }
  .person__first { font-weight: 700; }
  .person__last { font-weight: 300; color: var(--orange-soft); }
  .person__title { font-size: 13px; color: var(--grey-text); margin-top: 2px; }

  .contacts { position: absolute; left: 22px; top: 190px; list-style: none; color: var(--white); font-size: 12.5px; }
  .contacts li { display: flex; align-items: center; gap: 8px; line-height: 20px; }
  .contacts svg { width: 11px; height: 11px; flex: none; }

  .products { position: absolute; left: 300px; top: 234px; list-style: none; color: var(--white); font-size: 13.5px; line-height: 19px; }

  .back-web { position: absolute; left: 120px; top: 200px; font-size: 14px; color: var(--teal); }
</style>
</head>
<body>

<section class="card card--front" aria-label="Business card front">
  <svg class="card__wave" viewBox="0 0 520 297" preserveAspectRatio="none" aria-hidden="true">
    <defs>
      <linearGradient id="edge-front" x1="0" x2="1" y1="0" y2="0">
        <stop offset="0" stop-color="#f7b51c"/>
        <stop offset="1" stop-color="#f08a24"/>
      </linearGradient>
    </defs>
    <path d="M0,150 C180,160 360,195 520,232 L520,297 L0,297 Z" fill="var(--teal)"/>
    <path d="M0,150 C180,160 360,195 520,232" fill="none" stroke="url(#edge-front)" stroke-width="3"/>
  </svg>

  <div class="brand">
    <span class="brand__dot"></span>
    <span class="brand__name">Verdmont Flow Solutions</span>
  </div>

  <div class="person">
    <p class="person__name"><span class="person__first">Ravi</span> <span class="person__last">Tanaka</span></p>
    <p class="person__title">Business Manager</p>
  </div>

  <ul class="contacts">
    <li><svg viewBox="0 0 12 12"><path d="M2 1h2.5l1 3-1.5 1a6 6 0 0 0 3 3l1-1.5 3 1V10a1 1 0 0 1-1 1A9 9 0 0 1 1 2a1 1 0 0 1 1-1z" fill="var(--yellow)"/></svg>xxx.xxxxx.xx</li>
    <li><svg viewBox="0 0 12 12"><rect x="1" y="2.5" width="10" height="7" rx="1" fill="var(--yellow)"/><path d="M1.5 3l4.5 3.5L10.5 3" fill="none" stroke="var(--teal)" stroke-width="1"/></svg>ravi.tanaka@verdmont-example.com</li>
    <li><svg viewBox="0 0 12 12"><circle cx="6" cy="6" r="5" fill="var(--yellow)"/><path d="M1 6h10M6 1c-2.5 3-2.5 7 0 10M6 1c2.5 3 2.5 7 0 10" fill="none" stroke="var(--teal)" stroke-width="0.8"/></svg>www.verdmont-example.com.my</li>
  </ul>

  <ul class="products">
    <li>Pumping technology</li>
    <li>Valve &amp; actuation</li>
    <li>Air moving technology</li>
  </ul>
</section>

<section class="card card--back" aria-label="Business card back">
  <svg class="card__wave" viewBox="0 0 520 297" preserveAspectRatio="none" aria-hidden="true">
    <defs>
      <linearGradient id="edge-back" x1="0" x2="1" y1="0" y2="0">
        <stop offset="0" stop-color="#f7b51c"/>
        <stop offset="1" stop-color="#f08a24"/>
      </linearGradient>
      <linearGradient id="band-back" x1="0" x2="1" y1="0" y2="1">
        <stop offset="0" stop-color="#1a4152"/>
        <stop offset="1" stop-color="#0e2c39"/>
      </linearGradient>
    </defs>
    <path d="M0,0 H520 V240 C380,205 190,110 0,90 Z" fill="url(#band-back)"/>
    <path d="M0,90 C190,110 380,205 520,240" fill="none" stroke="url(#edge-back)" stroke-width="3"/>
  </svg>

  <div class="brand">
    <span class="brand__dot"></span>
    <span class="brand__name">Verdmont Flow Solutions</span>
  </div>

  <p class="back-web">www.verdmont-example.com.my</p>
</section>

</body>
</html>
```